business card for law firm that reflects the web site -www.MarlaQuentby.com. That is pleasant to read

We need a business card for a small law firm. Your company designed our logo - tree of life - which I can provide to the designers. The card should be on both sides. Use the coloring from the web site (www.MarlaQuentby.com) and logo (I have several formats). I am attaching the logo, but not sure what format to use.

First side name of firm: Law Office of M.K. Quentby, P.A. 4819 West Pallisor, Suite 300, Phoenix, AZ 85016, Phone: 602.555.3841, Fax: 602.555.7290, web site: www.MarlaQuentby.com, email: MQuentby@MarlaQuentby.com.
Marla K. Quentby Bankruptcy and Foreclosure Attorney & Counselor.
Back side (perhaps vertical) the logo and then Notes with lines. At the bottom: Proud to help people and small businesses file for bankruptcy protection. We are a debt relief agency.
Updates

I have several versions of the logo. Will be happy to share whatever you need. Added Sunday, April 3, 2016

Target Market(s)

everyone

Industry/Entity Type

Legal

Contact Information for Business Card

I prefer something unique (rounded edges, design that adopts my web site - www.MarlaQuentby.com.

Font styles to use
Serif

Requirements
Must have
• First side name of firm: Law Office of M.K. Quentby, P.A. 4819 West Pallisor, Suite 300, Phoenix, AZ 85016, Phone: 602.555.3841, Fax: 602.555.7290, web site: www.MarlaQuentby.com, email: MQuentby@MarlaQuentby.com.
• Marla K. Quentby Bankruptcy and Foreclosure Attorney & Counselor.
• Back side (perhaps vertical) the logo and then Notes with lines. At the bottom: Proud to help people and small businesses file for bankruptcy protection. We are a debt relief agency.
• Green and brown colors that reflect the web site: www.MarlaQuentby.com
Should not have
• Type so small that older people cannot read.

```html
<!DOCTYPE html>
<html lang="en">
<head>
<meta charset="utf-8">
<title>M.K. Quentby, P.A. — Business Card</title>
<link href="https://fonts.googleapis.com/css2?family=Cinzel:wght@400;600;700&display=swap" rel="stylesheet">
<style>
  :root {
    --bg: #e9e6e1;
    --brown: #3a2016;
    --brown-deep: #2f1a11;
    --green: #24472a;
    --green-deep: #1d3a22;
    --cream: #f2ece1;
    --ring: #e8e1d4;
  }
  * { box-sizing: border-box; margin: 0; padding: 0; }
  html, body { width: 1200px; height: 900px; overflow: hidden; }
  body {
    background: var(--bg);
    font-family: "Cinzel", serif;
    color: var(--cream);
    position: relative;
  }
  .card {
    position: absolute;
    left: 250px;
    width: 700px;
    height: 400px;
    border-radius: 28px;
    overflow: hidden;
    box-shadow: 0 10px 28px rgba(0,0,0,.22);
  }
  .card-front { top: 30px; background: var(--brown); }
  .card-back { top: 470px; background: var(--green); }

  /* logo stand-in */
  .mark {
    position: absolute;
    border-radius: 50%;
    background: var(--green-deep);
    border: 5px solid var(--ring);
    display: flex; align-items: center; justify-content: center;
    text-align: center;
  }
  .mark-name {
    font-family: "Cinzel", serif;
    font-weight: 600;
    color: var(--cream);
    line-height: 1.2;
  }

  /* front */
  .watermark {
    position: absolute; left: 300px; top: 18px;
    width: 250px; height: 250px; border-radius: 50%;
    border: 3px solid rgba(255,255,255,.05);
    display: flex; align-items: center; justify-content: center;
  }
  .watermark span { font-size: 26px; font-weight: 600; color: rgba(255,255,255,.05); }
  .front-mark { left: 44px; top: 150px; width: 128px; height: 128px; }
  .front-mark .mark-name { font-size: 17px; }
  .firm-pre { position: absolute; left: 192px; top: 175px; font-size: 19px; letter-spacing: .5px; }
  .firm-name { position: absolute; left: 192px; top: 198px; font-size: 50px; font-weight: 700; letter-spacing: 1px; white-space: nowrap; }
  .firm-name small { font-size: 16px; font-weight: 600; }
  .mission {
    position: absolute; left: 44px; right: 40px; top: 305px;
    font-size: 19px; line-height: 1.35; letter-spacing: .6px; text-transform: uppercase;
  }

  /* back */
  .band { position: absolute; left: 0; right: 0; background: var(--brown); }
  .band-upper { top: 128px; height: 82px; }
  .band-lower { top: 255px; height: 85px; }
  .person { position: absolute; right: 40px; top: 22px; text-align: right; }
  .person-name { font-size: 27px; letter-spacing: 1px; font-variant: small-caps; line-height: 1.2; margin-bottom: 4px; }
  .person-title { font-size: 16px; letter-spacing: .8px; font-variant: small-caps; line-height: 1.3; }
  .back-mark { right: 56px; top: 110px; width: 130px; height: 130px; }
  .back-mark .mark-name { font-size: 17px; }
  .contact { position: absolute; left: 36px; top: 262px; list-style: none; }
  .contact li {
    display: flex; align-items: center; gap: 9px;
    font-size: 16px; line-height: 18px; letter-spacing: .5px; font-variant: small-caps;
  }
  .contact svg { width: 12px; height: 12px; fill: var(--cream); flex: none; }
  .address {
    position: absolute; left: 36px; top: 348px;
    font-size: 18px; line-height: 1.25; letter-spacing: .8px; font-variant: small-caps;
  }
</style>
</head>
<body>

<section class="card card-front" aria-label="Card front">
  <div class="watermark" aria-hidden="true"><span>M.K. Quentby</span></div>
  <div class="mark front-mark"><span class="mark-name">M.K.<br>Quentby</span></div>
  <p class="firm-pre">Law Office of</p>
  <h1 class="firm-name">M.K. QUENTBY, <small>P.A.</small></h1>
  <p class="mission">Proud to help people and small businesses file for bankruptcy protection. We are a debt relief agency.</p>
</section>

<section class="card card-back" aria-label="Card back">
  <div class="band band-upper"></div>
  <div class="band band-lower"></div>

  <div class="person">
    <h2 class="person-name">Marla K. Quentby</h2>
    <p class="person-title">Bankruptcy and</p>
    <p class="person-title">Foreclosure Attorney &amp; Counselor</p>
  </div>

  <div class="mark back-mark"><span class="mark-name">M.K.<br>Quentby</span></div>

  <ul class="contact">
    <li><svg viewBox="0 0 12 12"><path d="M2.5 0.8 4.3 3 3.4 4.4c.8 1.7 2.2 3.1 3.9 3.9l1.4-.9 2.2 1.8-.9 2C5.2 11 1 6.8.8 1.7z"/></svg>602.555.3841</li>
    <li><svg viewBox="0 0 12 12"><rect x="3" y="0.5" width="6" height="3.5"/><rect x="0.5" y="4.5" width="11" height="5" rx="1"/><rect x="3" y="9" width="6" height="2.5"/></svg>602.555.7290</li>
    <li><svg viewBox="0 0 12 12"><path d="M0.5 2h11v8h-11z M1.5 3v.3L6 6.5l4.5-3.2V3z" fill-rule="evenodd"/></svg>MQuentby@MarlaQuentby.com</li>
    <li><svg viewBox="0 0 12 12"><circle cx="6" cy="6" r="5.5"/><path d="M0.5 6h11M6 .5c-2.5 3-2.5 8 0 11M6 .5c2.5 3 2.5 8 0 11" stroke="#3a2016" stroke-width=".8" fill="none"/></svg>www.MarlaQuentby.com</li>
  </ul>

  <div class="address">
    <p>4819 West Pallisor</p>
    <p>Suite 300, Phoenix, AZ 85016</p>
  </div>
</section>

</body>
</html>
```